Marlow Crest Group (Real Estate and Investment)

A high end, clean design.
We are a real estate company with sales, asset management and investment divisions. We want to use a black and white scheme which is really high end feel. The back of the card can just be the logo (black background with the white writing) as we will probably emboss this when we print)

Target Market(s)

High level investors, high end houses for sale

Industry/Entity Type

Business

Contact Information for Business Card

Name, position, phone number and email address
Glen Varley, Managing Director, 0437259064 and glen@marlowcrest-example.com.au

Requirements
Must have
• Back of the card to be the black background with the white writing (as per the attached images). Would like the capacity to emboss the writing and logo

```html
<!DOCTYPE html>
<html lang="en">
<head>
<meta charset="utf-8">
<title>Marlow Crest Group – Business Card</title>
<link rel="stylesheet" href="https://fonts.googleapis.com/css2?family=Montserrat:wght@300&family=Open+Sans:wght@400;600&display=swap">
<style>
  :root {
    --ink: #1f1e1f;
    --paper: #ffffff;
    --stage: #e9e7e4;
    --muted: #3a393a;
    --radius: 20px;
  }
  * { box-sizing: border-box; margin: 0; padding: 0; }
  html, body { width: 1200px; height: 1200px; overflow: hidden; }
  body {
    background: var(--stage);
    display: flex;
    flex-direction: column;
    align-items: center;
    justify-content: center;
    gap: 64px;
    font-family: "Open Sans", Arial, sans-serif;
  }
  .card {
    width: 760px;
    height: 440px;
    border-radius: var(--radius);
    overflow: hidden;
    box-shadow: 0 6px 18px rgba(0,0,0,0.15);
  }

  /* Back of card */
  .card-back {
    background: var(--ink);
    color: var(--paper);
    display: flex;
    flex-direction: column;
    align-items: center;
    justify-content: center;
    gap: 34px;
  }
  .brand-mark {
    width: 150px; height: 150px;
    border: 2px solid currentColor;
    border-radius: 50%;
  }
  .brand-name {
    font-family: "Montserrat", Arial, sans-serif;
    font-weight: 300;
    font-size: 44px;
    letter-spacing: 1px;
    text-transform: uppercase;
  }

  /* Front of card */
  .card-front {
    display: grid;
    grid-template-columns: 48% 52%;
    grid-template-rows: 1fr 1fr;
  }
  .cell {
    display: flex;
    flex-direction: column;
    align-items: center;
    justify-content: center;
    text-align: center;
  }
  .cell--light { background: var(--paper); color: var(--ink); }
  .cell--dark { background: var(--ink); color: var(--paper); }

  .profile-icon {
    width: 62px; height: 70px;
    background: var(--ink);
    border-radius: 10px 10px 4px 4px;
    margin-bottom: 18px;
  }
  .person-name { font-size: 30px; font-weight: 400; letter-spacing: 0.5px; }
  .person-role { font-size: 16px; color: var(--muted); margin-top: 4px; letter-spacing: 0.3px; }

  .contact-icon { margin-bottom: 22px; }
  .contact-phone { font-size: 26px; letter-spacing: 1px; }
  .contact-email { font-size: 17px; }

  .cell--brand { gap: 26px; }
  .cell--brand .brand-mark { width: 100px; height: 100px; }
  .cell--brand .brand-name { font-size: 28px; }
</style>
</head>
<body>

  <section class="card card-back" aria-label="Card back">
    <div class="brand-mark" aria-hidden="true"></div>
    <p class="brand-name">Marlow Crest Group</p>
  </section>

  <section class="card card-front" aria-label="Card front">
    <div class="cell cell--light">
      <div class="profile-icon" role="img" aria-label="Profile icon"></div>
      <p class="person-name">Glen Varley</p>
      <p class="person-role">Managing Director</p>
    </div>

    <div class="cell cell--dark">
      <svg class="contact-icon" width="56" height="56" viewBox="0 0 24 24" aria-hidden="true">
        <path fill="currentColor" d="M6.6 10.8c1.4 2.8 3.8 5.1 6.6 6.6l2.2-2.2c.3-.3.7-.4 1-.2 1.1.4 2.3.6 3.6.6.6 0 1 .4 1 1V20c0 .6-.4 1-1 1C10.6 21 3 13.4 3 4c0-.6.4-1 1-1h3.5c.6 0 1 .4 1 1 0 1.3.2 2.5.6 3.6.1.3 0 .7-.2 1l-2.3 2.2z"/>
        <path fill="none" stroke="currentColor" stroke-width="1.6" stroke-linecap="round" d="M14.5 6.5a4 4 0 0 1 3 3M15 2.8a7.5 7.5 0 0 1 6.2 6.2"/>
      </svg>
      <p class="contact-phone">0437259064</p>
    </div>

    <div class="cell cell--dark">
      <svg class="contact-icon" width="66" height="50" viewBox="0 0 66 50" aria-hidden="true">
        <rect x="0" y="0" width="66" height="50" fill="currentColor"/>
        <path d="M3 3 L33 28 L63 3" fill="none" stroke="#1f1e1f" stroke-width="4"/>
        <path d="M3 47 L24 24 M63 47 L42 24" fill="none" stroke="#1f1e1f" stroke-width="4"/>
      </svg>
      <p class="contact-email">glen@marlowcrest-example.com.au</p>
    </div>

    <div class="cell cell--light cell--brand">
      <div class="brand-mark" aria-hidden="true"></div>
      <p class="brand-name">Marlow Crest Group</p>
    </div>
  </section>

</body>
</html>
```